Personal Injury Law Firm Marketing Postcards

Looking for 4 different high quality graphic postcards (print on both sides of 4"x6" postcard to market a Personal Injury Lawyer (Walter Dunmore). These will be placed on cars and in stores on stands. My photo and/or stock images.... We are targeting People who have been injured in automobile accidents, motorcycle accidents, slip and fall (wet/greasy floors indoors in supermarkets, restaurants, etc., snow and ice outdoors on sidewalks) trip and fall cases on dangerous staircases. indoor/outdoor, dog bite injuries. ( I like the use of stock images of these type of injury causing accidents. You can use following language "Serving People Injured in NY & NJ" . Millions of Dollars Recovered, Free Consultation and No Fee Unless We Recover Money! Phone number to be displayed (555) 614-3082 "call or text" Available 24 hours a day 7 days per week. May also want to mention that we can take over your case from another lawyer if you are not satisfied with your current attorney. There should be a small space in corner which has a space for my marketing person to handwrite in their reference code.

Target Market(s)

18-75 years old - densely populated major city

Industry/Entity Type

Legal

Font styles to use
Other font styles liked:
• Please use logo style that I uploaded.. Please do not just cut parts of my website out and use them. Do not use LOGO from my website

Colors
0054AA
0677BA
7BADD7
CADEEF
E8F1F8
00AB8E
00BBA5
67D7C9
C6EFE9
E9F9F6

Requirements
Must have
• Professional Appearance

```html
<!DOCTYPE html>
<html lang="en">
<head>
<meta charset="utf-8">
<title>Walter Dunmore Postcards</title>
<link href="https://fonts.googleapis.com/css2?family=Oswald:wght@400;500&family=Montserrat:wght@800&display=swap" rel="stylesheet">
<style>
  :root{
    --navy:#162c5b;
    --gold:#d7ac6b;
    --white:#ffffff;
    --stage:#d3d3d3;
    --rule:#555555;
    --photo-warm:#8a6048;
    --photo-dark:#3a2a22;
  }
  *{margin:0;padding:0;box-sizing:border-box}
  html,body{width:1200px;height:1200px;overflow:hidden;background:var(--stage)}
  .postcard{position:absolute;left:214px;width:773px;height:494px;overflow:hidden;background:var(--white)}
  .postcard--front{top:77px}
  .postcard--back{top:629px;background:var(--navy)}
  .postcard svg.shapes{position:absolute;inset:0;width:773px;height:494px}
  .txt{position:absolute;white-space:nowrap;line-height:1}
  .brand-name{font-family:"Oswald",sans-serif;font-weight:500;text-transform:uppercase;color:var(--gold);transform:translateX(-50%);letter-spacing:1px}
  .cond{font-family:"Oswald",sans-serif;font-weight:500;text-transform:uppercase}
  .bold-sans{font-family:"Montserrat",sans-serif;font-weight:800}
  .gold{color:var(--gold)}
  .navy{color:var(--navy)}
  .white{color:var(--white)}
  .injury-list{position:absolute;left:46px;top:200px;list-style:none}
  .injury-list li{font-family:"Oswald",sans-serif;font-weight:400;text-transform:uppercase;color:var(--white);font-size:15px;line-height:22.3px;letter-spacing:.6px}
  .injury-list li::before{content:"";display:inline-block;width:4px;height:4px;border-radius:50%;background:var(--gold);margin:0 6px 3px 0;vertical-align:middle}
  .icon{display:inline-block;vertical-align:middle}
</style>
</head>
<body>

<section class="postcard postcard--front">
  <svg class="shapes" viewBox="0 0 773 494">
    <defs>
      <linearGradient id="photoTone" x1="0" y1="0" x2="1" y2="1">
        <stop offset="0" stop-color="var(--photo-warm)"/>
        <stop offset=".55" stop-color="#6b4a3a"/>
        <stop offset="1" stop-color="var(--photo-dark)"/>
      </linearGradient>
    </defs>
    <path d="M498,0 Q220,260 500,494 L773,494 L773,0 Z" fill="var(--navy)"/>
    <rect x="0" y="213" width="368" height="85" fill="var(--navy)"/>
    <rect x="150" y="435" width="370" height="59" fill="var(--navy)"/>
    <polygon points="150,435 168,435 192,464.5 168,494 150,494 174,464.5" fill="var(--white)"/>
    <polygon points="0,435 150,435 174,464.5 150,494 0,494" fill="var(--gold)"/>
    <path d="M552,0 Q240,260 507,494" fill="none" stroke="var(--gold)" stroke-width="4"/>
    <path d="M562,0 Q250,260 512,494 L773,494 L773,0 Z" fill="url(#photoTone)" role="img" aria-label="Portrait photo of the attorney in a navy suit"/>
  </svg>

  <div class="txt brand-name" style="left:174px;top:150px;font-size:32px">Walter Dunmore</div>

  <div class="txt cond gold" style="left:15px;top:229px;font-size:24px">Serving People Injured in NY &amp; NJ</div>
  <div class="txt cond white" style="left:15px;top:256px;font-size:22px">Millions of Dollars Recovered</div>

  <div class="txt cond navy" style="left:19px;top:319px;font-size:25px;line-height:29px">Free Consultation and No Fee<br>Unless We Recover Money!</div>

  <div class="txt cond navy" style="left:30px;top:396px;font-size:18px">
    <svg class="icon" width="26" height="26" viewBox="0 0 26 26" aria-hidden="true">
      <circle cx="13" cy="13" r="11" fill="none" stroke="var(--gold)" stroke-width="2"/>
      <path d="M8 13 l3.5 3.5 L18 9" fill="none" stroke="var(--gold)" stroke-width="2" stroke-linecap="round"/>
    </svg>
    <span style="vertical-align:middle;margin-left:4px">Available 24 hours a day 7 days per week</span>
  </div>

  <div class="txt bold-sans navy" style="left:20px;top:454px;font-size:22px">CALL US!</div>
  <div class="txt bold-sans white" style="left:200px;top:451px;font-size:25px">
    <svg class="icon" width="24" height="24" viewBox="0 0 24 24" aria-hidden="true">
      <circle cx="12" cy="12" r="12" fill="var(--gold)"/>
      <path d="M8.5 6.5 l2 2.6 -1.2 1.4 c.8 1.7 2.1 3 3.8 3.8 l1.4-1.2 2.6 2 -1.2 2 c-4.5-.4-8.1-4-8.5-8.5 z" fill="var(--navy)"/>
    </svg>
    <span style="vertical-align:middle">(555) 614-3082</span>
  </div>
</section>

<section class="postcard postcard--back">
  <svg class="shapes" viewBox="0 0 773 494">
    <rect x="0" y="423" width="470" height="71" fill="var(--gold)"/>
    <path d="M496,0 Q222,262 456,494 L773,494 L773,0 Z" fill="var(--gold)"/>
    <path d="M520,0 Q240,262 466,494 L773,494 L773,0 Z" fill="var(--white)"/>
    <path d="M526,0 Q248,262 472,494 L773,494 L773,0 Z" fill="var(--navy)"/>
    <path d="M536,0 Q260,262 480,494 L773,494 L773,0 Z" fill="var(--white)"/>
    <g stroke="var(--rule)" stroke-width="1.5">
      <line x1="433" y1="198" x2="720" y2="198"/>
      <line x1="433" y1="248" x2="720" y2="248"/>
      <line x1="433" y1="298" x2="720" y2="298"/>
      <line x1="433" y1="348" x2="720" y2="348"/>
    </g>
  </svg>

  <div class="txt brand-name" style="left:134px;top:92px;font-size:24px">Walter Dunmore</div>

  <div class="txt cond gold" style="left:46px;top:152px;font-size:16px;line-height:18px;letter-spacing:.5px">The Most Common Types of<br>Personal Injuries</div>

  <ul class="injury-list">
    <li>Motor Vehicle Accidents</li>
    <li>Work-Related Accidents</li>
    <li>Head Injuries</li>
    <li>Unsafe Products</li>
    <li>Animal Attacks</li>
    <li>Medical Malpractice</li>
    <li>Nursing Home Abuse</li>
    <li>Unsafe Properties</li>
  </ul>

  <div class="txt cond white" style="left:45px;top:399px;font-size:15px;letter-spacing:.5px">You may be entitled to money! Call us!</div>

  <div class="txt bold-sans navy" style="left:60px;top:437px;font-size:24px">
    <svg class="icon" width="22" height="22" viewBox="0 0 24 24" aria-hidden="true">
      <circle cx="12" cy="12" r="12" fill="var(--navy)"/>
      <path d="M8.5 6.5 l2 2.6 -1.2 1.4 c.8 1.7 2.1 3 3.8 3.8 l1.4-1.2 2.6 2 -1.2 2 c-4.5-.4-8.1-4-8.5-8.5 z" fill="var(--gold)"/>
    </svg>
    <span style="vertical-align:middle">(555) 614-3082</span>
  </div>
  <div class="txt bold-sans navy" style="left:63px;top:467px;font-size:15px;letter-spacing:2px">WWW.DUNMORELEGAL.COM</div>
</section>

</body>
</html>
```